Business Card Design Project

Use our current logo. Clean design.

Industry/Entity Type

Business

Requirements
Must have
• Marisela DUBRANCQ
M. Law
Managing Partner

Alpenvorsa AG
Kornhalmweg 214
CH-3097 Liebefeld

M. +41 79 412 56 27
T. +41 31 928 44 10
F. +41 31 928 44 19

m.dubrancq@alpenvorsa-example.com
www.alpenvorsa-example.com

```html
<!DOCTYPE html>
<html lang="en">
<head>
<meta charset="utf-8">
<title>Alpenvorsa AG – Business Card</title>
<link rel="stylesheet" href="https://fonts.googleapis.com/css2?family=Tinos:wght@400;700&display=swap">
<style>
  :root {
    --page: #ffffff;
    --card: #231f20;
    --ink: #ffffff;
    --ink-soft: #e6e6e6;
    --muted: #6b6869;
    --muted-dark: #57534f;
  }
  * { margin: 0; padding: 0; box-sizing: border-box; }
  html, body {
    width: 1200px;
    height: 848px;
    overflow: hidden;
    background: var(--page);
  }
  body {
    position: relative;
    font-family: "Tinos", "Times New Roman", serif;
    color: var(--ink);
  }
  .card {
    position: absolute;
    top: 333px;
    width: 520px;
    height: 273px;
    background: var(--card);
    overflow: hidden;
  }
  .card--front { left: 56px; }
  .card--back { left: 610px; }

  .wordmark {
    position: absolute;
    font-family: "Tinos", "Times New Roman", serif;
    font-weight: 400;
    color: var(--ink);
    letter-spacing: 0.06em;
    white-space: nowrap;
    transform: translateX(-50%);
  }
  .card--front .wordmark {
    left: 260px;
    top: 96px;
    font-size: 34px;
  }
  .card--back .wordmark {
    left: 407px;
    top: 122px;
    font-size: 28px;
  }

  .front-url {
    position: absolute;
    left: 0;
    right: 0;
    top: 214px;
    text-align: center;
    font-size: 11px;
    font-weight: 700;
    letter-spacing: 0.55em;
    color: var(--muted-dark);
  }

  .contact {
    position: absolute;
    left: 25px;
    top: 24px;
    font-size: 11px;
    line-height: 13.5px;
    color: var(--ink-soft);
  }
  .contact__name {
    font-size: 16px;
    line-height: 16px;
    font-weight: 400;
    color: var(--ink);
  }
  .contact__first { font-weight: 700; }
  .contact__degree { font-size: 10px; margin-left: 3px; }
  .contact__role {
    margin-top: 2px;
    font-size: 10px;
    font-weight: 700;
    color: var(--muted);
  }
  .contact__phones { margin-top: 22px; }
  .contact__address { margin-top: 18px; }
  .contact__email { margin-top: 27px; }

  .back-url {
    position: absolute;
    left: 25px;
    top: 241px;
    font-size: 10px;
    font-weight: 700;
    letter-spacing: 0.04em;
    color: var(--muted-dark);
  }
</style>
</head>
<body>
  <section class="card card--front" aria-label="Card front">
    <div class="wordmark">ALPENVORSA</div>
    <div class="front-url">www.alpenvorsa-example.com</div>
  </section>

  <section class="card card--back" aria-label="Card back">
    <div class="contact">
      <h1 class="contact__name"><span class="contact__first">Marisela</span> DUBRANCQ,<span class="contact__degree">M. Law</span></h1>
      <p class="contact__role">Managing Partner</p>
      <p class="contact__phones">
        M. +41 79 412 56 27<br>
        T. +41 31 928 44 10<br>
        F. +41 31 928 44 19
      </p>
      <p class="contact__address">
        Alpenvorsa AG<br>
        Kornhalmweg 214<br>
        CH-3097 Liebefeld
      </p>
      <p class="contact__email">m.dubrancq@alpenvorsa-example.com</p>
    </div>
    <div class="wordmark">ALPENVORSA</div>
    <div class="back-url">www.alpenvorsa-example.com</div>
  </section>
</body>
</html>
```